Business card design needed

My company does everything from wiring up your exisiting entertainment system, to installing a complete new system for you. We can mount your plasma on the wall, install an aerial point for you, setup some surround sound in your outdoor area or install a new cinema room in your house. Any Audio or Visual requirements you may have we can provide these for you. If you want to have a party to remember at your place or just some chilled sounds by the pool, we can give you just the right size system.

Industry/Entity Type

Entertainment

Contact Information for Business Card

The Tune Crew
Colin Pemberton
e| colin@thetunecrew.com.au
w| www.thetunecrew.com.au
m| 0412 576 208

Requirements
Must have
• The logo that i have uploaded is just a starter...something similar to this but not exact or any new suggestions you have would be great too. Colour choice we are pretty easy on we did think Red and Yellow but happy to take advice, something that stands out from the rest i guess.

```html
<!DOCTYPE html>
<html lang="en">
<head>
<meta charset="utf-8">
<title>The Tune Crew – Business Card</title>
<link rel="stylesheet" href="https://fonts.googleapis.com/css2?family=Arimo:wght@400;700&display=swap">
<style>
  :root {
    --page-bg: #ffffff;
    --card-bg: #ffffff;
    --brand-red: #ed1c24;
    --brand-grey: #8b8786;
    --name-grey: #545454;
    --label-grey: #5a5a5a;
    --detail-grey: #8c8c8c;
    --card-edge: #3a3a3a;
    --white: #ffffff;
  }
  html, body {
    margin: 0;
    padding: 0;
    width: 1200px;
    height: 1000px;
    overflow: hidden;
    background: var(--page-bg);
    font-family: "Arimo", Arial, sans-serif;
  }
  .card {
    position: absolute;
    left: 37px;
    top: 120px;
    width: 1065px;
    height: 613px;
    background: var(--card-bg);
    border: 1px solid var(--card-edge);
    box-sizing: border-box;
    box-shadow: 3px 5px 5px rgba(0, 0, 0, 0.55);
  }
  .brand-mark {
    position: absolute;
    left: 58px;
    top: 52px;
    margin: 0;
    font-weight: 700;
    font-size: 64px;
    line-height: 0.95;
    letter-spacing: -2px;
    color: var(--brand-grey);
  }
  .contact {
    position: absolute;
    left: 53px;
    top: 318px;
  }
  .contact-name {
    margin: 0 0 20px;
    font-weight: 700;
    font-size: 40px;
    letter-spacing: 4px;
    color: var(--name-grey);
  }
  .contact-line {
    margin: 0;
    font-size: 36px;
    line-height: 66px;
    color: var(--detail-grey);
    letter-spacing: 0.5px;
  }
  .contact-label {
    font-weight: 700;
    color: var(--label-grey);
  }
  .feature-panel {
    position: absolute;
    left: 611px;
    top: 0;
    right: 0;
    bottom: 0;
    background: var(--brand-red);
    overflow: hidden;
  }
  .feature-name {
    position: absolute;
    left: 10px;
    top: 228px;
    margin: 0;
    font-weight: 700;
    font-size: 128px;
    line-height: 0.98;
    letter-spacing: -5px;
    color: var(--white);
  }
</style>
</head>
<body>
  <div class="card">
    <p class="brand-mark">The Tune<br>Crew</p>

    <div class="contact">
      <p class="contact-name">Colin Pemberton</p>
      <p class="contact-line"><span class="contact-label">e|</span> colin@thetunecrew.com.au</p>
      <p class="contact-line"><span class="contact-label">w|</span> www.thetunecrew.com.au</p>
      <p class="contact-line"><span class="contact-label">m|</span> 0412 576 208</p>
    </div>

    <div class="feature-panel">
      <p class="feature-name">The Tune<br>Crew</p>
    </div>
  </div>
</body>
</html>
```